New look and feel for investment website

Hi

Our website needs a crisp and professional look and feel applying to it. Here’s the address: http://www.brightplinth.co.uk. Since posting the brief yesterday (Tuesday, 16 August), we've reduced the amount of content on the home page, which should make life a little easier for you. We will come back later today, with some points of reference in terms of sites we like the look of. (See below)

17 August, 1.20pm GMT. OK, comments generally on the designs submitted so far. Please keep in mind that images of graphs, piles of coins, paper money and pretty females are not what is required. Better to think in terms of abstract imagery instead. Ratios? Circles? Relationships? Patterns? Not money,sex,graphs etc. Hope that helps.

For guidance on look and feel, please refer to these sites, which we like:

http://www.morvelle.co.uk/
http://www.qz.com/
https://www.harrowfieldtamsin.com
https://www.pirelconcerns.com
https://www.kvantule.com
Updates

Here's the Tall Beacons logo created in AI CS5.

Our market is professional financial advisers and relatively sophisticated private investors. The look and feel therefore should be slick and sophisticated - not 'lively' and lightweight, more like a banking site. Please read the brief again where we've added a list of websites that we really like the look of to get a better feel for what we're looking for. Thanks once again, we appreciate the work you're putting in.

It's essential that all the elements that are on the current home page be included on all new designs. 

We use a device in our e-mails which you may wish to incorporate in your design.

Target Market(s)

Professional financial advisers. People who know about investment and money.

Industry/Entity Type

Investment

Requirements
Should not have
• Graphs or people.

```html
<!DOCTYPE html>
<html lang="en">
<head>
<meta charset="utf-8">
<title>Tall Beacons – Investment</title>
<link href="https://fonts.googleapis.com/css2?family=Arimo:wght@400;700&family=PT+Sans:wght@400;700&display=swap" rel="stylesheet">
<style>
:root{
  --red:#a3272e;
  --red-dark:#861d23;
  --red-deep:#6f171c;
  --grey-light:#f0f0f0;
  --grey-band:#dcdcdc;
  --grey-nav:#cfcfcf;
  --grey-mid:#bfbfbf;
  --grey-dark:#a9a9a9;
  --ink:#222;
  --ink-soft:#555;
  --white:#fff;
}
*{margin:0;padding:0;box-sizing:border-box}
html,body{width:1178px;height:1200px;overflow:hidden;background:var(--white)}
body{position:relative;font-family:"Arimo",Arial,sans-serif;color:var(--ink)}
a{color:inherit}
.abs{position:absolute}

/* left column */
.sidebar{left:0;top:0;width:380px;height:1092px;background:var(--grey-nav)}
.top-tabs{left:0;top:0;width:380px;height:34px;display:flex;background:var(--red-deep)}
.top-tabs a{display:flex;align-items:center;justify-content:center;color:var(--white);text-decoration:none;font-size:20px;border-right:2px solid var(--white);height:34px}
.top-tabs a:nth-child(1){width:140px}
.top-tabs a:nth-child(2){width:128px;font-weight:700}
.top-tabs a:nth-child(3){width:112px;border-right:0}
.brand{left:0;top:34px;width:380px;height:200px;background:var(--grey-light);text-align:center}
.brand-name{position:absolute;left:0;right:0;top:68px;font-size:50px;font-weight:400;color:var(--ink)}
.brand-tag{position:absolute;left:0;right:0;top:132px;font-size:16px;color:var(--ink-soft)}
.register{left:0;top:234px;width:380px;height:71px;background:var(--grey-band);color:var(--red);font-size:33px;display:flex;align-items:center;justify-content:center}
.nav{left:0;top:331px;width:380px;list-style:none}
.nav li{position:relative;height:49px}
.nav a{position:absolute;right:66px;bottom:6px;font-size:27px;color:#6a6a6a;text-decoration:none}
.nav li::after{content:"";position:absolute;left:0;width:315px;bottom:0;height:1px;background:#9c9c9c}
.nav .num{position:absolute;left:339px;top:-14px;font-size:16px;font-weight:700;color:var(--red)}
.promo{left:0;top:697px;width:380px;height:191px;background:var(--grey-mid)}
.promo-photo{left:0;top:0;width:170px;height:191px;background:linear-gradient(160deg,#c9a88c,#8f5a3e 60%,#ddd)}
.promo p{position:absolute;left:189px;top:22px;width:152px;font-family:"PT Sans",sans-serif;font-size:15.5px;line-height:20px;color:#444}
.promo p b{color:#333}
.btn-more{display:flex;width:86px;height:26px;background:var(--red);color:var(--white);font-size:14px;font-weight:700;text-decoration:none;border:1px solid #888}
.btn-more span{flex:1;display:flex;align-items:center;justify-content:center}
.btn-more em{width:22px;background:#ddd;display:flex;align-items:center;justify-content:center}
.promo .btn-more{position:absolute;left:255px;top:140px}
.contact{left:0;top:888px;width:380px;height:204px;background:var(--grey-dark)}
.contact-map{left:40px;top:23px;width:115px;height:58px;background:radial-gradient(ellipse at 40% 50%,#8f8f8f,#a9a9a9 70%)}
.contact h3{position:absolute;left:169px;top:28px;font-size:17px;color:#333}
.contact address{position:absolute;left:169px;top:54px;font-style:normal;font-size:16px;line-height:21px;color:#333}
.phone{left:131px;top:124px;display:flex;align-items:center;gap:8px;font-size:27px;color:var(--red)}
.phone i{width:31px;height:31px;background:var(--red);border-radius:5px;display:flex;align-items:center;justify-content:center}

/* right column */
.hero-photo{left:382px;top:0;width:796px;height:282px;background:linear-gradient(135deg,#3f4a5c,#8c98ab 45%,#c9ced8 70%,#9aa3b2)}
.hero-band{left:382px;top:282px;width:796px;height:36px;background:var(--red);color:var(--white);font-size:27px;letter-spacing:-1px;text-align:right;padding-right:40px;line-height:36px}
.hero-strip{left:382px;top:318px;width:796px;height:102px;background:linear-gradient(180deg,#6e5860,#c9b4b6 35%,#aab 100%)}
.hero-cta{left:382px;top:320px;width:796px;text-align:right;padding-right:60px;color:var(--white);font-size:15px}
.hero-cta b{font-size:29px;letter-spacing:-1px;margin-left:12px}
.welcome-photo{left:382px;top:420px;width:330px;height:277px;background:linear-gradient(90deg,#c2a58b,#e8ddd5 70%,#fff)}
.welcome{left:654px;top:450px;width:480px}
.welcome::before{content:"";position:absolute;left:0;top:2px;width:3px;height:54px;background:var(--red)}
.welcome h1{margin-left:17px;font-size:33px;color:var(--red);line-height:34px}
.welcome h2{margin-left:35px;font-weight:400;font-size:26px;color:#777;line-height:30px}
.welcome p{margin:6px 0 0 23px;width:445px;font-family:"PT Sans",sans-serif;font-size:16px;line-height:21px;color:#555}
.welcome p b{color:#333}
.links{left:805px;top:602px;list-style:none;font-family:"PT Sans",sans-serif;font-size:15px;color:var(--red)}
.links li{display:flex;align-items:center;gap:10px;height:25px}
.links i{width:11px;height:11px;border:1px solid #666;display:inline-block;position:relative}
.links i::after{content:"";position:absolute;left:2px;top:4px;width:5px;height:1px;background:#666}
.divider-h{left:382px;top:697px;width:796px;height:2px;background:#ddd}
.about{left:382px;top:699px;width:446px;height:393px}
.about h2{position:absolute;left:36px;top:13px;font-size:33px;color:var(--red)}
.about h3{position:absolute;left:36px;top:49px;font-weight:400;font-size:20px;color:#888}
.about-text{position:absolute;left:36px;top:83px;width:252px;font-family:"PT Sans",sans-serif;font-size:15.5px;line-height:20px;color:#444}
.about-text b{color:#222}
.about-more{position:absolute;left:36px;top:250px;width:380px;font-family:"PT Sans",sans-serif;font-size:15.5px;line-height:20px;color:#444}
.about-photo{position:absolute;left:305px;top:89px;width:106px;height:142px;border:1px solid #999;background:linear-gradient(180deg,#e4e6ea,#7a808c)}
.about .btn-more{position:absolute;left:323px;top:333px}
.divider-v{left:827px;top:699px;width:2px;height:393px;background:#ddd}
.ratios{left:829px;top:699px;width:349px;height:393px;padding:23px 0 0 8px}
.ratios h2{font-weight:400;font-size:43px;color:var(--red);margin-left:18px}
.ratios ul{list-style:none;margin-top:14px;width:330px;font-family:"PT Sans",sans-serif;font-size:14.5px;line-height:22px;color:var(--red-dark)}

/* footer */
.footer{left:0;top:1092px;width:1178px;height:108px;background:var(--red)}
.footer-top{left:0;top:1092px;width:1178px;height:18px;background:var(--red-deep)}
.footer-nav{left:40px;top:1118px;display:flex;list-style:none}
.footer-nav li{height:62px;display:flex;align-items:center;padding:0 17px;border-right:1px solid #d58a8e;color:var(--white);font-size:16px}
.footer-nav li:first-child{padding-left:18px}
.footer-legal{right:52px;top:1123px;color:var(--white);font-size:15px;text-align:right;line-height:22px}
.footer-legal a{font-weight:700}
</style>
</head>
<body>

<div class="abs sidebar"></div>
<nav class="abs top-tabs"><a href="#">Log in</a><a href="#">FAQs</a><a href="#">Watch list</a></nav>

<div class="abs brand">
  <div class="brand-name">Tall Beacons</div>
  <div class="brand-tag">the best that suits your needs</div>
</div>

<div class="abs register">Registration</div>

<ul class="abs nav">
  <li><span class="num">01</span><a href="#">Home</a></li>
  <li><span class="num">02</span><a href="#">Two Minute Guide</a></li>
  <li><span class="num">03</span><a href="#">Other key numbers</a></li>
  <li><span class="num">04</span><a href="#">Back tested results</a></li>
  <li><span class="num">05</span><a href="#">History of all trades</a></li>
  <li><span class="num">06</span><a href="#">About our analyses</a></li>
  <li><span class="num">07</span><a href="#">About value investing</a></li>
</ul>

<section class="abs promo">
  <div class="abs promo-photo" role="img" aria-label="Photo of a smiling advisor on the phone"></div>
  <p><b>Lorem ipsum</b> sit amet, consectetuer adipiscing elit, sed diam nonummy nibh euismod tincidunt.</p>
  <a class="btn-more" href="#"><span>more</span><em>»</em></a>
</section>

<section class="abs contact">
  <div class="abs contact-map" role="img" aria-label="World map silhouette"></div>
  <h3>New-York. USA</h3>
  <address>StreetStreetStreetStreet<br>StreetStreet Street<br>StreetStreet Street</address>
  <div class="abs phone"><i><svg width="18" height="18" viewBox="0 0 24 24"><path fill="#fff" d="M6.6 10.8a15 15 0 0 0 6.6 6.6l2.2-2.2c.3-.3.7-.4 1-.2 1.1.4 2.3.6 3.6.6.6 0 1 .4 1 1V20c0 .6-.4 1-1 1A17 17 0 0 1 3 4c0-.6.4-1 1-1h3.5c.6 0 1 .4 1 1 0 1.3.2 2.5.6 3.6.1.3 0 .7-.2 1z"/></svg></i>000-000-000</div>
</section>

<div class="abs hero-photo" role="img" aria-label="Photo of two business people shaking hands"></div>
<div class="abs hero-band">The best that suits your needs</div>
<div class="abs hero-strip" role="img" aria-label="Blurred office backdrop"></div>
<div class="abs hero-cta">take the best corporate deal <b>click here</b></div>

<div class="abs welcome-photo" role="img" aria-label="Photo of a support agent wearing a headset"></div>
<section class="abs welcome">
  <h1>Welcome</h1>
  <h2>to our business company web site</h2>
  <p><b>Well, we have a pleasant surprise for you: you couldn't be further from the truth.</b>, consectetuer adipiscing elit, sed diam nonummy nibh euismod tincidunt ut</p>
</section>
<ul class="abs links">
  <li><i></i>Current &amp; year to date performance</li>
  <li><i></i>The Halden 1000 and the Corvex 500 index</li>
</ul>

<div class="abs divider-h"></div>

<section class="abs about">
  <h2>About us</h2>
  <h3>business company web site</h3>
  <p class="about-text"><b>Something different...</b><br>You may well be thinking that Tall Beacons is just another one of those banal share recommenda-tion sites sprinkled with the usual idiotic and patronising platitudes, gross exaggerations, silly get-rich-quick promises</p>
  <div class="about-photo" role="img" aria-label="Photo of a business team"></div>
  <p class="about-more">and all the other stuff and nonsense you associate with the black art of share-tipping…</p>
  <a class="btn-more" href="#"><span>more</span><em>»</em></a>
</section>

<div class="abs divider-v"></div>

<section class="abs ratios">
  <h2>Ratios</h2>
  <ul>
    <li>Average, annualised compound return over to : 23.57 %</li>
    <li>So far this year, the portfolio's return is 13.49 %:</li>
    <li>Worst ever annual loss: -1.48 %; best ever annual gain: 69.77 %</li>
    <li>Average return per trade including losing trades: 24.44 %</li>
    <li>Maximum number of winning/losing trades in a row: 11/4.</li>
  </ul>
</section>

<footer>
  <div class="abs footer"></div>
  <div class="abs footer-top"></div>
  <ul class="abs footer-nav">
    <li><a href="#">Payments</a></li>
    <li><a href="#">Guarantee</a></li>
    <li><a href="#">Links</a></li>
    <li><a href="#">Downloads</a></li>
    <li><a href="#">Contact</a></li>
  </ul>
  <div class="abs footer-legal"><a href="#">Terms of Use</a> | <a href="#">Privacy Statement</a><br>© 2011 Your Corporation. All rights reserved</div>
</footer>

</body>
</html>
```